Business Card Design

We are a project managment company specializing in Interior fitout
PVH is for Commercial, Domestic, Industial - we provide managment to these industries and see the projects through design to contruction
Would like an area on the back of the card where peoplr can write notes
Thinking laser lines and architectural finishes
Colour theme at the moment is light grey and red although im open to any colour/design scheme

Industry/Entity Type

Business

Contact Information for Business Card

PVH Ventures
Brett Lamonte
Managing Director
0487215694
brett@pvhventures-example.com.au

```html
<!DOCTYPE html>
<html lang="en">
<head>
<meta charset="utf-8">
<title>Tarnell Ventures — Business Card</title>
<link href="https://fonts.googleapis.com/css2?family=Nunito+Sans:wght@400;600&family=Open+Sans:wght@400&display=swap" rel="stylesheet">
<style>
  :root {
    --page: #ececea;
    --card: #ffffff;
    --charcoal: #666666;
    --ink: #58595b;
    --red: #f00000;
    --red-fold: #c8282d;
    --white: #ffffff;
  }
  * { margin: 0; padding: 0; box-sizing: border-box; }
  html, body {
    width: 1200px; height: 1200px; overflow: hidden;
    background: var(--page);
  }
  .canvas { position: relative; width: 1200px; height: 1200px; }
  .card {
    position: absolute; left: 170px; width: 860px; height: 530px;
    background: var(--card);
    box-shadow: 0 10px 30px rgba(0,0,0,0.18);
    overflow: hidden;
  }
  .card--front { top: 45px; }
  .card--back { top: 625px; }

  .wordmark {
    display: flex; align-items: center; gap: 14px;
    font-family: "Nunito Sans", sans-serif; font-weight: 600;
    color: var(--ink); white-space: nowrap; letter-spacing: 0.5px;
  }
  .wordmark__square { width: 0.5em; height: 0.5em; background: var(--red); }
  .card--front .wordmark {
    position: absolute; left: 50%; top: 50%;
    transform: translate(-50%, -50%); font-size: 56px;
  }
  .card--back .wordmark {
    position: absolute; left: 56px; bottom: 42px; font-size: 34px; gap: 10px;
  }

  .back-panel { position: absolute; inset: 0; }

  .name-tag {
    position: absolute; left: 451px; top: 106px; width: 337px; height: 90px;
    background: var(--red); color: var(--white);
    text-align: right; padding: 8px 46px 0 0;
  }
  .name-tag__name { font-family: "Open Sans", sans-serif; font-size: 33px; line-height: 42px; letter-spacing: 0.5px; }
  .name-tag__role { font-family: "Nunito Sans", sans-serif; font-size: 20px; line-height: 28px; letter-spacing: 0.5px; }

  .contact {
    position: absolute; right: 72px;
    display: flex; align-items: center; gap: 8px;
    font-family: "Nunito Sans", sans-serif; font-size: 22px; letter-spacing: 0.6px;
    color: var(--white); white-space: nowrap;
  }
  .contact--phone { top: 318px; }
  .contact--email { top: 446px; font-size: 18px; letter-spacing: 0.3px; right: 60px; }
  .contact svg { display: block; }
</style>
</head>
<body>
<div class="canvas">

  <section class="card card--front">
    <div class="wordmark"><span class="wordmark__square"></span>Tarnell Ventures</div>
  </section>

  <section class="card card--back">
    <svg class="back-panel" width="860" height="530" viewBox="0 0 860 530">
      <polygon points="622,0 860,0 860,530 367,530" fill="var(--charcoal)"/>
      <polygon points="451,196 527,196 505,238" fill="var(--red-fold)"/>
    </svg>

    <div class="name-tag">
      <div class="name-tag__name">Brett Lamonte</div>
      <div class="name-tag__role">Managing Director</div>
    </div>

    <div class="contact contact--phone">
      <svg width="16" height="22" viewBox="0 0 16 22" aria-hidden="true">
        <path d="M5 1 L8 6 L6 8 Q6 12 10 15 L12 13 L15 17 L12 20 Q2 16 2 4 Z" fill="var(--red)"/>
      </svg>
      <span>0487215694</span>
    </div>

    <div class="contact contact--email">
      <svg width="24" height="16" viewBox="0 0 26 18" aria-hidden="true">
        <rect x="0" y="0" width="26" height="18" fill="var(--red)"/>
        <path d="M1 1 L13 10 L25 1 M1 17 L10 8 M25 17 L16 8" stroke="var(--charcoal)" stroke-width="1.6" fill="none"/>
      </svg>
      <span>brett@tarnellventures-example.com.au</span>
    </div>

    <div class="wordmark"><span class="wordmark__square"></span>Tarnell Ventures</div>
  </section>

</div>
</body>
</html>
```